Allied Health team of Physiotherapists & Occupational Therapists seek a business card design

We have our new logo, we now need our new business cards and stationary. Willowmere: Oedema & Family Clinic is seeking a generic card design to represent our whole team and individual cards for each therapist that incorporates our new logo to communicate our holistic approach that is calming, nuturing, supportive and welcoming.
Our Physiotherapists and Occupational Therapists assess, treat and provide education for people who are at risk of or who have lymphoedema. This is often as a result of treatment for cancer. We provide pre-operative and post-operative management and cancer rehabilitation in our Pilates studio. Our team also consists of Physiotherapists who have a strong interest in pelvic floor and continence management for both men and women.

Target Market(s)

Mainly women health conscious

Industry/Entity Type

Allied Health: Physiotherapy / Occupational Therapy

Contact Information for Business Card

Address: 14 Tannerly Ave Larkhaven 3287 Phone: 84317756 fax: 8431 7759 Email: info@willowmerecareco.com.au Website: willowmerecareco.com.au Facebook address: facebook.com/WillowmereOedemaAndFamilyCareCentre. Room to write appointments. Individual cards need to have name, office email and individual email and professional details

Requirements
Must have
• Logo as per uploaded documents

```html
<!DOCTYPE html>
<html lang="en">
<head>
<meta charset="utf-8">
<title>Willowmere: Oedema &amp; Family Clinic – Business Card</title>
<link rel="stylesheet" href="https://fonts.googleapis.com/css2?family=Cinzel:wght@400&family=Open+Sans:wght@400;600&family=Montserrat:wght@400;800&display=swap">
<style>
  :root {
    --peach: #f6a46f;
    --peach-soft: #f8b38a;
    --sage: #b9c6b7;
    --ink: #4a4a4a;
    --paper: #ffffff;
    --backdrop: #6f6f6f;
    --dots: #7a7a7a;
  }
  * { box-sizing: border-box; margin: 0; padding: 0; }
  html, body { width: 1200px; height: 800px; overflow: hidden; }
  body {
    background: var(--backdrop);
    display: flex; align-items: center; justify-content: center; gap: 40px;
    font-family: "Open Sans", Arial, sans-serif;
  }
  .card {
    position: relative; width: 540px; height: 309px;
    background: var(--paper); border-radius: 18px; overflow: hidden;
    box-shadow: 0 8px 24px rgba(0,0,0,.25);
  }

  /* Front */
  .brand {
    position: absolute; top: 34px; right: 34px; width: 190px;
    display: flex; align-items: center; gap: 10px;
  }
  .brand-dot { flex: none; width: 14px; height: 14px; border-radius: 50%; background: var(--sage); }
  .brand-name {
    font-family: "Cinzel", Georgia, serif; font-weight: 400;
    color: var(--peach); font-size: 15px; line-height: 1.35;
  }
  .person { position: absolute; left: 34px; top: 150px; }
  .person-name {
    font-family: "Cinzel", Georgia, serif; color: var(--peach);
    font-size: 24px; letter-spacing: .5px;
  }
  .person-role { color: var(--ink); font-size: 12px; margin-top: 2px; }
  .rule { position: absolute; left: 34px; right: 34px; top: 206px; height: 1px; background: var(--peach); }
  .contact {
    position: absolute; left: 34px; right: 34px; top: 222px;
    display: flex; justify-content: space-between;
    color: var(--ink); font-size: 12.5px; line-height: 1.45;
  }
  .edge-band { position: absolute; left: 0; right: 0; bottom: 0; height: 12px; display: flex; }
  .edge-band .warm { flex: 62; background: var(--peach); }
  .edge-band .cool { flex: 38; background: var(--sage); }

  /* Back */
  .book-online {
    position: absolute; top: 26px; right: 28px;
    background: var(--peach); color: var(--paper);
    font-family: "Montserrat", Arial, sans-serif; font-weight: 800; font-size: 14px;
    padding: 5px 16px; border-radius: 8px;
  }
  .appt-title {
    position: absolute; top: 34px; left: 30px;
    font-family: "Montserrat", Arial, sans-serif; font-weight: 800;
    color: var(--peach); font-size: 22px;
  }
  .appt-rows { position: absolute; left: 30px; right: 28px; top: 82px; }
  .appt-row {
    display: flex; align-items: baseline; gap: 6px; height: 34px;
    font-family: "Montserrat", Arial, sans-serif; font-size: 13px; color: var(--peach);
  }
  .appt-fill { border-bottom: 1.5px dotted var(--dots); transform: translateY(-3px); }
  .appt-fill.date { flex: 1.3; }
  .appt-fill.time { flex: 1; }
  .web-band {
    position: absolute; left: 0; right: 0; bottom: 28px; height: 38px;
    background: var(--peach-soft); color: var(--paper);
    display: flex; align-items: center; justify-content: center;
    font-family: "Montserrat", Arial, sans-serif; font-size: 14px; letter-spacing: 4px;
  }
</style>
</head>
<body>
  <section class="card card-front">
    <div class="brand">
      <span class="brand-dot"></span>
      <span class="brand-name">Willowmere: Oedema &amp; Family Clinic</span>
    </div>
    <div class="person">
      <div class="person-name">Marla Fenwick</div>
      <div class="person-role">Physiotherapist</div>
    </div>
    <div class="rule"></div>
    <div class="contact">
      <div class="contact-address">14 Tannerly Ave<br>Larkhaven 3287</div>
      <div class="contact-phone">P: 8431 7756<br>F: 8431 7759</div>
      <div class="contact-online">info@willowmerecareco.com.au<br>www.willowmerecareco.com.au</div>
    </div>
    <div class="edge-band"><span class="warm"></span><span class="cool"></span></div>
  </section>

  <section class="card card-back">
    <div class="appt-title">Appointment</div>
    <div class="book-online">Book Online</div>
    <div class="appt-rows">
      <div class="appt-row"><span>Date :</span><span class="appt-fill date"></span><span>Time :</span><span class="appt-fill time"></span><span>AM/PM</span></div>
      <div class="appt-row"><span>Date :</span><span class="appt-fill date"></span><span>Time :</span><span class="appt-fill time"></span><span>AM/PM</span></div>
      <div class="appt-row"><span>Date :</span><span class="appt-fill date"></span><span>Time :</span><span class="appt-fill time"></span><span>AM/PM</span></div>
      <div class="appt-row"><span>Date :</span><span class="appt-fill date"></span><span>Time :</span><span class="appt-fill time"></span><span>AM/PM</span></div>
    </div>
    <div class="web-band">WILLOWMERECARECO.COM.AU</div>
  </section>
</body>
</html>
```